Marketing graphics & images for Shopify store

I need someone to create some graphics/images for a coffee sales shopify storefront incorporating my existing logo and want variations on the logo colour so it blends with background images. Freelancer is to provide suitable coffee product related images and designs. Want a catalogue of images i can rotate and use on the storefront.

The tagline on the storefront page " a fresh start to your day" will change - i will update brief accordingly.

Font styles to use
Script

Requirements
Must have
• A variety of images sizes and graphics to be rotated for website marketing purposes.

Also would like some additional logo files with varying colors - ie black version, white version. Darker more chocolate brown version. Need to be logo quality

```html
<!DOCTYPE html>
<html lang="en">
<head>
<meta charset="utf-8">
<title>Hot &amp; Special Delicious Coffee – Banner</title>
<link href="https://fonts.googleapis.com/css2?family=Bebas+Neue&family=Montserrat:wght@600;700&display=swap" rel="stylesheet">
<style>
  :root{
    --backdrop:#4a231a;
    --banner-edge:#2a130c;
    --banner-mid:#8c4535;
    --yellow:#ffd800;
    --ink:#2b1610;
    --white:#ffffff;
    --line:rgba(255,255,255,0.08);
    --logo:#8a5a3c;
  }
  *{margin:0;padding:0;box-sizing:border-box}
  html,body{width:1200px;height:600px;overflow:hidden;background:var(--backdrop)}
  .canvas{position:relative;width:1200px;height:600px;background:var(--backdrop)}
  .banner{
    position:absolute;left:89px;top:110px;width:1022px;height:380px;overflow:hidden;
    background:
      radial-gradient(ellipse 60% 90% at 58% 45%, var(--banner-mid) 0%, #6a3024 45%, var(--banner-edge) 100%);
    box-shadow:0 6px 10px rgba(0,0,0,0.45);
  }
  .banner__lines{position:absolute;inset:0}
  .brand{
    position:absolute;left:26px;top:36px;display:flex;align-items:center;gap:7px;
    font-family:"Montserrat",sans-serif;font-weight:700;font-size:14px;color:var(--logo);letter-spacing:.3px;
  }
  .brand__dot{width:26px;height:26px;border-radius:50%;background:var(--logo)}
  .headline{position:absolute;left:0;top:0;width:100%;height:100%;font-family:"Bebas Neue",sans-serif}
  .headline__top{
    position:absolute;left:210px;top:86px;width:192px;text-align:center;
    font-size:40px;line-height:1;color:var(--white);letter-spacing:.5px;
  }
  .headline__ribbon{position:absolute;left:148px;top:129px;width:310px;height:72px}
  .headline__main{
    position:absolute;left:148px;top:129px;width:310px;height:72px;
    display:flex;align-items:center;justify-content:center;
    font-size:70px;line-height:1;color:var(--ink);padding-top:6px;letter-spacing:.5px;
  }
  .headline__bottom{
    position:absolute;left:210px;top:204px;width:192px;text-align:center;
    font-size:56px;line-height:1;color:var(--white);letter-spacing:.5px;
  }
  .burst{position:absolute;top:144px;width:48px;height:42px}
  .burst--left{left:104px}
  .burst--right{left:452px;transform:scaleX(-1)}
  .cta{
    position:absolute;left:239px;top:301px;width:141px;height:38px;border-radius:19px;
    background:var(--yellow);display:flex;align-items:center;justify-content:center;
    font-family:"Montserrat",sans-serif;font-weight:700;font-size:14px;color:var(--ink);letter-spacing:.2px;
  }
  .product-photo{
    position:absolute;left:490px;top:0;width:450px;height:380px;
    background:radial-gradient(ellipse 50% 50% at 55% 50%, #2a140c 0%, rgba(60,28,18,.75) 55%, rgba(60,28,18,0) 100%);
  }
  .badge{
    position:absolute;left:863px;top:47px;width:96px;height:96px;border-radius:50%;
    background:var(--yellow);display:flex;flex-direction:column;align-items:center;justify-content:center;
    font-family:"Bebas Neue",sans-serif;color:var(--ink);font-size:31px;line-height:.95;
  }
</style>
</head>
<body>
<div class="canvas">
  <section class="banner">
    <svg class="banner__lines" width="1022" height="380" viewBox="0 0 1022 380">
      <g stroke="var(--line)" stroke-width="2">
        <line x1="35" y1="185" x2="135" y2="85"/>
        <line x1="190" y1="65" x2="225" y2="30"/>
        <line x1="0" y1="325" x2="60" y2="265"/>
        <line x1="125" y1="380" x2="190" y2="315"/>
        <line x1="170" y1="260" x2="205" y2="225"/>
        <line x1="850" y1="65" x2="905" y2="10"/>
        <line x1="880" y1="220" x2="1022" y2="95"/>
        <line x1="960" y1="350" x2="1000" y2="310"/>
        <line x1="850" y1="380" x2="910" y2="320"/>
      </g>
    </svg>

    <div class="brand"><span class="brand__dot"></span>Café Marinheiro</div>

    <div class="product-photo" role="img" aria-label="Top view of a white cup of black coffee on a saucer surrounded by scattered roasted coffee beans"></div>

    <div class="headline">
      <div class="headline__top">Hot &amp; Special</div>
      <svg class="headline__ribbon" viewBox="0 0 310 72" aria-hidden="true">
        <polygon points="0,0 310,0 296,36 310,72 0,72 14,36" fill="var(--yellow)"/>
      </svg>
      <div class="headline__main">Delicious</div>
      <div class="headline__bottom">Coffee</div>
      <svg class="burst burst--left" viewBox="0 0 48 42" aria-hidden="true">
        <path d="M2 22 Q20 17 44 21 Q20 27 2 22Z" fill="var(--yellow)"/>
        <path d="M20 2 Q34 8 42 16 Q30 12 20 2Z" fill="var(--white)"/>
        <path d="M20 40 Q34 34 42 27 Q30 31 20 40Z" fill="var(--white)"/>
      </svg>
      <svg class="burst burst--right" viewBox="0 0 48 42" aria-hidden="true">
        <path d="M2 22 Q20 17 44 21 Q20 27 2 22Z" fill="var(--yellow)"/>
        <path d="M20 2 Q34 8 42 16 Q30 12 20 2Z" fill="var(--white)"/>
        <path d="M20 40 Q34 34 42 27 Q30 31 20 40Z" fill="var(--white)"/>
      </svg>
    </div>

    <a class="cta">SHOP NOW</a>

    <div class="badge"><span>Save</span><span>10%</span></div>
  </section>
</div>
</body>
</html>
```